Plakat für LRB Erlangen
Zielgruppe
Die LRB Erlangen ist der Kreisverband der Liberalen Reform Bewegung in Erlangen.
Aufgabenstellung
Es soll ein Plakat (DinA0, Hochformat) designed werden, welches als Basisplakat für verschiedene Veranstaltungen der LRB Erlangen dienen soll. Um dies zu gewährleisten, soll das Plakat eine zentrale freie Fläche mit einer hellen Hintergrundfarbe (z.B. weiß) besitzen, die groß genug ist, um ein ausgedrucktes DinA3 Papier mit Veranstaltungsinformationen darauf zu befestigen.
Das Basisplakat, welches sich an der CI der LRB orientieren soll, soll darüber hinaus das Logo des Kreisverbands Erlangen sowie den Slogan "Bei Ihnen. Direkt. Vor Ort" enthalten. Das LRB-Blau kann bei der Gestaltung des Plakats gerne als Hauptfarbe fungieren.
Ebenfalls enthalten sein soll der Vermerk im Sinne des Pressgesetzes: "VisdP: LRB Erlangen, Tannenhof-Str. 17b, 91052 Erlangen".
Die fertigen Datei soll auch in einem Format vorliegen, das mit Adobe Photoshop oder Illustrator geöffnet und bearbeitet werden kann.
Vielen herzlichen Dank schon mal für Ihre kreativen Entwürfe!

```html
<!DOCTYPE html>
<html lang="de">
<head>
<meta charset="utf-8">
<title>LRB Erlangen – Basisplakat</title>
<link rel="stylesheet" href="https://fonts.googleapis.com/css2?family=Open+Sans:ital,wght@0,400;0,700;1,700&display=swap">
<style>
  :root {
    --lrb-blau: #05b0fd;
    --lrb-blau-dunkel: #0a8fd6;
    --akzent-gruen: #1ee51e;
    --weiss: #ffffff;
    --platzhalter-grau: #9a9a9a;
    --rahmen-grau: #8c8c8c;
    --text-dunkel: #1a1a1a;
  }
  * { margin: 0; padding: 0; box-sizing: border-box; }
  html, body { width: 849px; height: 1200px; overflow: hidden; background: var(--weiss); }
  .poster {
    position: relative;
    width: 849px;
    height: 1200px;
    background: var(--weiss);
    font-family: "Open Sans", Arial, sans-serif;
    overflow: hidden;
  }
  .brand {
    position: absolute;
    top: 58px;
    right: 54px;
    display: flex;
    align-items: center;
    gap: 12px;
    color: var(--lrb-blau);
    font-weight: 700;
    font-size: 50px;
    line-height: 1;
    letter-spacing: 0.5px;
  }
  .brand-dot {
    width: 22px;
    height: 22px;
    border-radius: 50%;
    background: var(--akzent-gruen);
  }
  .hero-band {
    position: absolute;
    left: 0;
    top: 220px;
    width: 849px;
    height: 567px;
    background: var(--lrb-blau);
  }
  .hero-graphic {
    position: absolute;
    left: 0;
    top: 0;
    width: 460px;
    height: 567px;
    background: radial-gradient(ellipse at 62% 55%, rgba(255,255,255,0.55) 0%, rgba(255,255,255,0.18) 45%, rgba(255,255,255,0) 75%);
  }
  .slogan {
    position: absolute;
    right: 33px;
    top: 133px;
    text-align: right;
    color: var(--weiss);
    font-weight: 700;
    font-style: italic;
    font-size: 68px;
    line-height: 104px;
    letter-spacing: -0.5px;
  }
  .event-area {
    position: absolute;
    left: 27px;
    top: 844px;
    width: 795px;
    height: 301px;
    border: 1px solid var(--rahmen-grau);
    background: var(--weiss);
    display: flex;
    align-items: center;
    justify-content: center;
  }
  .event-placeholder {
    font-family: Arial, "Open Sans", sans-serif;
    color: var(--platzhalter-grau);
    font-size: 86px;
    font-weight: 400;
    letter-spacing: 1px;
    margin-top: 8px;
  }
  .footer-rule {
    position: absolute;
    left: 0;
    top: 1172px;
    width: 849px;
    height: 3px;
    background: var(--akzent-gruen);
  }
  .imprint {
    position: absolute;
    left: 0;
    top: 1176px;
    width: 849px;
    text-align: center;
    color: var(--text-dunkel);
    font-size: 20px;
    line-height: 24px;
    letter-spacing: 0.5px;
  }
  .imprint-sep { margin: 0 8px; }
</style>
</head>
<body>
<div class="poster">
  <div class="brand">
    <span class="brand-dot"></span>
    <span class="brand-name">LRB Erlangen</span>
  </div>

  <section class="hero-band">
    <div class="hero-graphic" role="img" aria-label="Dekoratives Punktraster in Weiß auf Blau"></div>
    <h1 class="slogan">Bei Ihnen.<br>Direkt.<br>Vor Ort.</h1>
  </section>

  <div class="event-area">
    <span class="event-placeholder">PLATZHALTER</span>
  </div>

  <div class="footer-rule"></div>
  <p class="imprint">VisdP: LRB Erlangen<span class="imprint-sep">•</span>Tannenhof-Str. 17b<span class="imprint-sep">•</span>91052 Erlangen</p>
</div>
</body>
</html>
```